Poster for Psychotherapy on Polyvagal theory

Poster is sketched out and I need a designer to design it. My sketch is very rough and just an idea. I do want creativity on it. If it could match the theme of my website style thats great. I do want it realisitic with acutal picutres not animated.. The poster is based on polyvagal theory and the visual is climging a mountain and mapping where you are at on the levels. So the levels 1-14 will be overlayed on the mountain. On my sketch those listed in green do not need to be on the poster but are instructions.

The poster will show three levels of the mountain. 1. base camp that is cold, lonely and immobility. 2. Climging the mountain which is acitiviating, hard, energetic,but can be angry too 3. The mountain top which is peaceful and a place for peaceful connection. Maybe a person on top, maybe?? An example of the ladder is on the website though we are changing the design to the mountain so don’t copy the website https://www.rosalindtverd.com/polyvagal-project

However on the website you will see the words your physiology in each box. I do want those on the poster. They can be a breaout arrow with those in it. This will be a large poster so using a lot of space is great.

Target Market(s)

Trauma psychotherapy clients

Industry/Entity Type

psychotherapy

Requirements
Must have
• great visuals realisitic, my logo at the bottom of page or somewhere on poster. this can be small. i will upload logo
Should not have
• animated

```html
<!DOCTYPE html>
<html lang="en">
<head>
<meta charset="utf-8">
<title>Climbing Polyvagal</title>
<link rel="stylesheet" href="https://fonts.googleapis.com/css2?family=Josefin+Sans:wght@400;600&family=DM+Serif+Display&display=swap">
<style>
  :root {
    --sky: #e6e3e0;
    --haze: #d4c7c0;
    --rock: #8f8a88;
    --rock-dark: #6d6b6d;
    --snow: #a9b7c4;
    --snow-deep: #8e9eae;
    --ventral: #1f7fc4;
    --rule-orange: #e08a3c;
    --sympathetic: #9b0d0d;
    --dorsal: #1d1d1d;
    --white: #ffffff;
  }
  html, body {
    margin: 0;
    padding: 0;
    width: 900px;
    height: 1200px;
    overflow: hidden;
    background: var(--sky);
  }
  .poster {
    position: relative;
    width: 900px;
    height: 1200px;
    overflow: hidden;
  }
  .mountain-photo {
    position: absolute;
    inset: 0;
    background:
      radial-gradient(ellipse 330px 640px at 450px 760px, rgba(95,92,94,0.75), rgba(95,92,94,0) 70%),
      linear-gradient(180deg, var(--sky) 0%, var(--sky) 22%, var(--haze) 45%, var(--rock) 62%, var(--snow) 78%, var(--snow-deep) 100%);
  }
  .layer {
    position: absolute;
    inset: 0;
  }
  .title { font-family: "Josefin Sans", sans-serif; font-weight: 400; font-size: 50px; fill: var(--ventral); letter-spacing: 1px; }
  .zone-name { font-family: "DM Serif Display", serif; font-size: 34px; fill: var(--white); }
  .zone-sub { font-family: "DM Serif Display", serif; font-size: 22px; fill: var(--white); }
  .state { font-family: "Josefin Sans", sans-serif; font-weight: 600; font-size: 20px; letter-spacing: 0.6px; }
  .level { font-family: "Josefin Sans", sans-serif; font-weight: 400; font-size: 26px; }
  .state.ventral, .level.ventral { fill: var(--ventral); }
  .state.sympathetic, .level.sympathetic { fill: var(--sympathetic); }
  .state.dorsal, .level.dorsal { fill: var(--dorsal); }
  .side-label { font-family: "Josefin Sans", sans-serif; font-weight: 600; font-size: 30px; letter-spacing: 1.5px; }
  .side-label.ventral { fill: var(--ventral); }
  .side-label.sympathetic { fill: var(--sympathetic); }
  .side-label.dorsal { fill: var(--dorsal); }
  .intervention-head { font-family: "Josefin Sans", sans-serif; font-size: 24px; fill: var(--ventral); letter-spacing: 0.8px; }
  .intervention { font-family: "Josefin Sans", sans-serif; font-size: 21px; letter-spacing: 0.6px; }
  .intervention.sympathetic { fill: var(--sympathetic); }
  .intervention.dorsal { fill: var(--dorsal); font-size: 19px; }
  .brand { font-family: "Josefin Sans", sans-serif; font-weight: 600; font-size: 18px; fill: var(--white); letter-spacing: 1px; }
</style>
</head>
<body>
<main class="poster">
  <div class="mountain-photo" role="img" aria-label="Photograph of a snowy mountain peak above the clouds, with a climber standing on the summit, arms raised"></div>

  <svg class="layer" width="900" height="1200" viewBox="0 0 900 1200" xmlns="http://www.w3.org/2000/svg">
    <defs>
      <path id="path-safe" d="M262 432 Q300 360 344 306"/>
      <path id="path-mobility" d="M78 772 L208 580"/>
      <path id="path-immobility" d="M30 1134 Q50 980 86 828"/>
    </defs>

    <text class="title" x="108" y="116">CLIMBING</text>
    <text class="title" x="518" y="118">POLYVAGAL</text>

    <text class="side-label ventral"><textPath href="#path-safe">I am safe</textPath></text>
    <polygon points="336,289 369,270 369,308" fill="var(--ventral)"/>
    <text class="side-label sympathetic"><textPath href="#path-mobility">Mobility  I can</textPath></text>
    <polygon points="190,555 222,536 222,574" fill="var(--sympathetic)"/>
    <text class="side-label dorsal"><textPath href="#path-immobility">Immobility    I can't</textPath></text>

    <g class="zone ventral-zone">
      <text class="zone-name" x="453" y="334" text-anchor="middle">Ventral Vagal</text>
      <text class="zone-sub" x="453" y="363" text-anchor="middle">Sense of Safety</text>
      <g stroke="var(--rule-orange)" stroke-width="1">
        <line x1="353" y1="382" x2="593" y2="382"/>
        <line x1="315" y1="421" x2="622" y2="421"/>
        <line x1="267" y1="458" x2="639" y2="458"/>
        <line x1="251" y1="495" x2="657" y2="495"/>
      </g>
      <text class="state ventral" x="316" y="413">Safe</text>
      <text class="level ventral" x="453" y="415" text-anchor="middle">14</text>
      <text class="state ventral" x="495" y="413">Connection</text>
      <text class="state ventral" x="316" y="449" textLength="112" lengthAdjust="spacingAndGlyphs">Compassion</text>
      <text class="level ventral" x="453" y="451" text-anchor="middle">13</text>
      <text class="state ventral" x="495" y="449">Flexible</text>
      <text class="state ventral" x="316" y="483">Open</text>
      <text class="level ventral" x="453" y="485" text-anchor="middle">12</text>
      <text class="state ventral" x="495" y="483">Grounded</text>
      <text class="state ventral" x="316" y="522">Playful</text>
      <text class="level ventral" x="453" y="524" text-anchor="middle">11</text>
      <text class="state ventral" x="495" y="522">Curious</text>
    </g>
    <rect x="231" y="532" width="454" height="5" fill="var(--sympathetic)"/>

    <g class="zone sympathetic-zone">
      <text class="zone-name" x="453" y="573" text-anchor="middle">Sympathetic</text>
      <text class="zone-sub" x="453" y="604" text-anchor="middle">Fight | Flight</text>
      <g stroke="var(--sympathetic)" stroke-width="1">
        <line x1="163" y1="647" x2="718" y2="647"/>
        <line x1="149" y1="683" x2="724" y2="683"/>
        <line x1="124" y1="722" x2="767" y2="722"/>
        <line x1="105" y1="763" x2="868" y2="763"/>
      </g>
      <text class="state sympathetic" x="316" y="638">Agitated</text>
      <text class="level sympathetic" x="453" y="640" text-anchor="middle">10</text>
      <text class="state sympathetic" x="495" y="638">On Edge</text>
      <text class="state sympathetic" x="316" y="673" textLength="102" lengthAdjust="spacingAndGlyphs">Frustration</text>
      <text class="level sympathetic" x="453" y="675" text-anchor="middle">9</text>
      <text class="state sympathetic" x="495" y="673">Worry</text>
      <text class="state sympathetic" x="316" y="714">Irritation</text>
      <text class="level sympathetic" x="453" y="716" text-anchor="middle">8</text>
      <text class="state sympathetic" x="495" y="714">Anxiety</text>
      <text class="state sympathetic" x="316" y="755">Anger</text>
      <text class="level sympathetic" x="453" y="757" text-anchor="middle">7</text>
      <text class="state sympathetic" x="495" y="755">Fear</text>
      <text class="state sympathetic" x="316" y="795">Rage</text>
      <text class="level sympathetic" x="453" y="793" text-anchor="middle">6</text>
      <text class="state sympathetic" x="495" y="795">Panic</text>
    </g>
    <rect x="19" y="804" width="867" height="6" fill="var(--dorsal)"/>

    <g class="zone dorsal-zone">
      <text class="zone-name" x="453" y="845" text-anchor="middle">Dorsal Vagal</text>
      <text class="zone-sub" x="453" y="871" text-anchor="middle">Freeze</text>
      <g stroke="var(--dorsal)" stroke-width="1">
        <line x1="126" y1="921" x2="704" y2="921"/>
        <line x1="126" y1="967" x2="704" y2="967"/>
        <line x1="126" y1="1015" x2="704" y2="1015"/>
        <line x1="126" y1="1064" x2="704" y2="1064"/>
        <line x1="126" y1="1108" x2="704" y2="1108"/>
      </g>
      <text class="state dorsal" x="316" y="899" textLength="118" lengthAdjust="spacingAndGlyphs">Unmotivated</text>
      <text class="level dorsal" x="455" y="898" text-anchor="middle">5</text>
      <text class="state dorsal" x="495" y="899">Low</text>
      <text class="state dorsal" x="316" y="946" textLength="117" lengthAdjust="spacingAndGlyphs">Helplessness</text>
      <text class="level dorsal" x="455" y="945" text-anchor="middle">4</text>
      <text class="state dorsal" x="495" y="946">Trapped</text>
      <text class="state dorsal" x="316" y="994">Depression</text>
      <text class="level dorsal" x="455" y="993" text-anchor="middle">3</text>
      <text class="state dorsal" x="495" y="994">Hopelessness</text>
      <text class="state dorsal" x="316" y="1043">Numbness</text>
      <text class="level dorsal" x="455" y="1042" text-anchor="middle">2</text>
      <text class="state dorsal" x="495" y="1043">Shut down</text>
      <text class="state dorsal" x="316" y="1092" textLength="128" lengthAdjust="spacingAndGlyphs">Disassociation</text>
      <text class="level dorsal" x="455" y="1090" text-anchor="middle">1</text>
      <text class="state dorsal" x="495" y="1092">Shame</text>
    </g>

    <g class="interventions">
      <polygon points="811,288 792,317 830,317" fill="var(--ventral)"/>
      <g stroke="var(--ventral)" stroke-width="1">
        <line x1="730" y1="330" x2="730" y2="377"/>
        <line x1="892" y1="330" x2="892" y2="377"/>
      </g>
      <text class="intervention-head" x="734" y="357">Interventions</text>

      <polygon points="811,488 792,521 830,521" fill="var(--sympathetic)"/>
      <g stroke="var(--sympathetic)" stroke-width="1">
        <line x1="730" y1="534" x2="730" y2="686"/>
        <line x1="892" y1="534" x2="892" y2="686"/>
      </g>
      <text class="intervention sympathetic" x="736" y="558">1. TIPP</text>
      <text class="intervention sympathetic" x="736" y="604">2. Self-Soothe</text>
      <text class="intervention sympathetic" x="736" y="646">3. Somatic</text>
      <text class="intervention sympathetic" x="736" y="674">Interventions</text>

      <polygon points="811,827 792,861 830,861" fill="var(--dorsal)"/>
      <g stroke="var(--dorsal)" stroke-width="1">
        <line x1="730" y1="816" x2="730" y2="1169"/>
        <line x1="892" y1="816" x2="892" y2="1169"/>
      </g>
      <text class="intervention dorsal" x="736" y="891">1. Eat &amp;</text>
      <text class="intervention dorsal" x="736" y="917">take medication</text>
      <text class="intervention dorsal" x="736" y="972">2. Move for</text>
      <text class="intervention dorsal" x="736" y="999">ten minutes</text>
      <text class="intervention dorsal" x="736" y="1061">3. Shower and</text>
      <text class="intervention dorsal" x="736" y="1088">brush teeth</text>
      <text class="intervention dorsal" x="736" y="1151">4. Call a friend</text>
    </g>

    <g class="brand-mark">
      <circle cx="404" cy="1176" r="6" fill="var(--white)"/>
      <text class="brand" x="416" y="1182">Summit Steps</text>
    </g>
  </svg>
</main>
</body>
</html>
```